Commercial Real Estate Executive Recruiting Firm Needs Business Card Design

We need a business card design for MARLOW | Executive Recruiting - an executive recruiting firm focused exclusively on the commercial real estate industry. We place professionals ranging from Analyst to the Executive Office covering all investment/finance disciplines (acquisitions, asset management, capital markets, etc.) in all product types (office, retail, multifamily, industrial, land, etc.). We have a passion for helping people (clients and candidates) and have a reputation for being open and honest in our recruiting - and yes, very successful. We have recently developed a new logo and would like to update our business cards as well. I've uploaded some information about our company that contains the new logo.

Target Market(s)

Commercial Real Estate professionals. Primarily in the US. These are typically, smart, driven professionals with finance degrees and MBAs. Primarily men between the ages of 25 and 55.

Industry/Entity Type

Real Estate

Font styles to use
Other font styles liked:
• The font for "MARLOW" is Blair ITC (Medium), and "executive recruiting" is Gotham (Book).

Requirements
Must have
• I like the idea of white background on one side and solid color (blue, black, etc.) on back of card.

Would like to utilize the fonts in the logo (to the extent possible) so as to not have too many fonts on card.
Nice to have
• I think the roles (i.e., Acquisitions, Asset Management, etc.,...) is probably likely best placed on the back side of the card with the logo maybe. See attached current business card for content.

```html
<!DOCTYPE html>
<html lang="en">
<head>
<meta charset="utf-8">
<title>MARLOW Executive Recruiting – Business Cards</title>
<link rel="stylesheet" href="https://fonts.googleapis.com/css2?family=Roboto+Condensed:wght@400;700&display=swap">
<style>
  :root {
    --canvas: #ecebe8;
    --card-white: #fbfbfb;
    --card-grey: #e9eaec;
    --ink: #3d4147;
    --brand-blue: #3f7cbd;
    --band-light: #5f98c8;
    --band-mid: #2f6aa5;
    --band-deep: #173a63;
    --band-text: #ffffff;
  }
  * { box-sizing: border-box; margin: 0; padding: 0; }
  html, body { width: 1200px; height: 1000px; overflow: hidden; }
  body {
    background: var(--canvas);
    font-family: "Roboto Condensed", sans-serif;
    position: relative;
  }
  .card {
    position: absolute;
    left: 240px;
    width: 720px;
    height: 411px;
    border-radius: 26px;
    overflow: hidden;
    background: linear-gradient(180deg, var(--card-white) 0%, var(--card-grey) 64%);
    box-shadow: 0 10px 26px rgba(0,0,0,0.18);
  }
  .card--front { top: 50px; }
  .card--back { top: 540px; }
  .band {
    position: absolute;
    left: 0; right: 0; bottom: 0;
    height: 36%;
    background: linear-gradient(90deg, var(--band-light) 0%, var(--band-mid) 45%, var(--band-deep) 100%);
  }
  .company-name {
    position: absolute;
    font-weight: 400;
    font-size: 32px;
    line-height: 1;
    color: var(--ink);
    white-space: nowrap;
  }
  .card--front .company-name { left: 50%; top: 148px; transform: translateX(-50%); }
  .card--back .company-name { left: 54px; top: 150px; }
  .person {
    position: absolute;
    right: 48px; top: 42px;
    text-align: right;
  }
  .person__name {
    font-size: 34px;
    line-height: 1;
    color: var(--brand-blue);
    font-weight: 400;
  }
  .person__name b { color: var(--ink); font-weight: 700; }
  .person__title { font-size: 15px; color: var(--ink); margin-top: 3px; }
  .contact {
    position: absolute;
    right: 26px; bottom: 22px;
    list-style: none;
    font-size: 15px;
    color: var(--band-text);
    text-align: right;
  }
  .contact li {
    display: flex;
    justify-content: flex-end;
    align-items: center;
    gap: 12px;
    line-height: 31px;
  }
  .contact svg { width: 15px; height: 15px; fill: var(--band-text); }
</style>
</head>
<body>

<section class="card card--front" aria-label="Card front">
  <p class="company-name">MARLOW | Executive Recruiting</p>
  <div class="band"></div>
</section>

<section class="card card--back" aria-label="Card back">
  <p class="company-name">MARLOW | Executive Recruiting</p>
  <div class="person">
    <p class="person__name">JORDAN<b>BLAKE</b></p>
    <p class="person__title">Vice President</p>
  </div>
  <div class="band"></div>
  <ul class="contact">
    <li>1480 Ridgemont Lane / Austin, Texas 78701
      <svg viewBox="0 0 16 16" aria-hidden="true"><path d="M8 1 1 7.5h2V15h4v-4h2v4h4V7.5h2z"/></svg>
    </li>
    <li>512-555-0147
      <svg viewBox="0 0 16 16" aria-hidden="true"><path d="M3.6 1.2 6 3.6 4.7 5.6c.9 2.2 2.9 4.3 5.2 5.2l2-1.3 2.4 2.4-1.6 2.3C7.4 14 2 8.6 1.3 2.8z"/></svg>
    </li>
    <li>www.marlowrecruiting.com
      <svg viewBox="0 0 16 16" aria-hidden="true"><circle cx="8" cy="8" r="6.5" fill="none" stroke="#fff" stroke-width="1.4"/><path d="M1.5 8h13M8 1.5c-3 3.5-3 9.5 0 13M8 1.5c3 3.5 3 9.5 0 13" fill="none" stroke="#fff" stroke-width="1.2"/></svg>
    </li>
  </ul>
</section>

</body>
</html>
```